Create an Event-Centric WordPress Website for NGO

1. Project Overview

- We represent "Zusammen für Brockelsdorf e.V.", a non-profit association. Our outdated website www.zfbev-beispiel.de shall get a proper replacement.

- The primary goal of our new site is to showcase and facilitate bookings for our cultural events, including concerts, theme nights, joint dinners and village festivals.

- Alongside event bookings, we plan to introduce the public to our history, values, leadership team, and news through a regularly updated blog.

- At a later stage we aim to integrate a user-friendly web shop based on WooCommerce, offering a range of up to 10 products related to our organization. This web-shop is not part of this project! The only relevant item is to include one menu item called "Shop" in the menu bar within the header.

2. Design Requirements

- The design should lean towards a sleek, welcoming, and slightly playful OnePage layout for the main page with additional pages as required.

- The color scheme should integrate the blue and red from our logo, as detailed in the attached brand board. However, deviations that enhance the design are welcome.

- Essential files like logos, photos, and texts are provided in the attachments.

- Emphasis should be on illustrating the community spirit, our events, and the emotions they evoke.

- Mobile first! Of course we like a great design both on desktops and smartphones. Nevertheless, if priorizaztion is needed, mobiles comes first.

3. Site Structure and Navigation

The website should be structured as follows:

**Main Page:**
- Opening with a Gallery/Video/Slogan.
- Upcoming Events.
- Counters to track event attendance or other metrics.
- Shoet description of what we do incl. mission Statements.
- Team Introduction.
- Top News Highlights.
- Contact Form.

**Additional Pages:**
- **About Us:** Detailing our history, a gallery, and a membership form.
- **Shop:** The content and setup is not part of this project and shall only be displayed as a menu item in the upper menu bar in the header.
- **Data Protection & Imprint:** Accessible via footer links.

Social media buttons for Facebook and Instagram should be prominently placed, preferably in the footer.

I am not really sure, if the design contest includes one page only. For the project please concentrate anyhow on the main page and we can then clarify further details.

4. Technical Requirements

- The site is to be fully developed in WordPress.

- Samples for initial design, including products, news, and events, are attached. However, the end design should accommodate easy edits and content additions. For the news the blog function within WordPress shall be used.

- Usability is paramount. Therefore, the Elementor plugin should be incorporated for easy edits without in-depth technical knowledge.

5. Event Management

- Events should have categories (e.g., concerts, dinner parties).

- Direct ticket booking with a cap on maximum participants is a must. Potential tools include the WordPress plugin GatherDesk or wordpress themes like Vorelt. This project only includes the design of the elements related to the event booking on the main page. The setup of the e-commerce functionality Inch. payment, etc. is not part of this project and will be sourced separately at a later stage.

6. Responsiveness & Speed

- The site must be mobile-responsive, ensuring a seamless experience across devices.

- Page load speed is crucial. Optimizations should be made to ensure swift page loads.

7. SEO & Optimization

- The website should be built with basic SEO principles in mind, ensuring improved visibility on search engines.

8. Post-Design

- Upon design completion, a subsequent project will cover the WordPress setup on our KARVO hosting platform and content addition.

- Continuous direct feedback will be provided throughout the design process to ensure clarity and minimize revisions.

- Post handover, we will manage the site in-house. No long-term maintenance is required from the designer.

9. Additional Notes

- We're open to design deviations if they lead to enhanced outcomes or usability.

10. Sample texts

Main Page:

Opening (Slogan)
[EN]: Slogan for the main opening.
[DE]: "Nachbarschaft spüren. In Brockelsdorf daheim!"
Upcoming Events (Event Descriptions)
2.1 Mara Quell
[EN]: Description for Mara Quell's event.
[DE]: "Mara kehrt zurück! Am 10.11.2023 erneut in der Holunderscheune. Lassen Sie sich von ihrem Mix aus Schlagern und Evergreens mitreißen."
2.2 Spanischer Abend
[EN]: Description for the Italian evening.
[DE]: "La Dolce Vita in Brockelsdorf. Am 21.11.2023 genießen wir in der Holunderscheune authentische italienische Spezialitäten in einer warmen Atmosphäre."
Metrics (Counters)
[EN]: Counters to showcase community metrics.
[DE]:
Mitglieder: "XXX stolze Mitglieder."
Events in 2023: "XXX Events bisher in diesem Jahr."
Besucher: "XXX glückliche Besucher bei unseren Veranstaltungen."
Short Description (Values and Mission)
[EN]: Short descriptions for the community values.
[DE]:
Miteinander in Brockelsdorf stärken: "Unsere Gemeinschaft ist unser Herzstück. Wir setzen uns dafür ein, dass jeder Einwohner in Brockelsdorf sich zugehörig und geschätzt fühlt."
Kulturelles Angebot schaffen: "Kultur belebt! Durch Veranstaltungen, Konzerte und Feste bereichern wir das kulturelle Leben in Brockelsdorf."
Füreinander da sein: "In guten wie in schlechten Zeiten – wir stehen zusammen. Egal ob jung oder alt, jeder wird in unserer Gemeinschaft unterstützt."
Team (Board Members)
[EN]: Introduction of the board members with photos and titles.
[DE]: "Unser engagiertes Team. Lernen Sie die Köpfe hinter 'Zusammen für Brockelsdorf e.V.' kennen."
News (Recent News Highlights)
[EN]: Short description of a recent news event.
[DE]: Sommerfest in Brockelsdorf: "Ein voller Erfolg! Mit über 400 Besuchern feierten wir am 21.06.2023 unser traditionelles Sommerfest inklusive Vogelschießen."
Contact Form (Contact Details)
[EN]: Contact form header and description.
[DE]: "Wir sind für Sie da! Haben Sie Fragen, Anregungen oder möchten Sie uns unterstützen? Kontaktieren Sie uns – wir freuen uns auf Ihre Nachricht."

Target Market(s)

Our target audience are the approx. 2.150 citizens of our village based in Germany, east of Hamburg. Many families with children, but also elderly people a singles. Also, foreigners, who are specially interested in our events are considered as our target audience.

Industry/Entity Type

NGO (cultural events for local village community)

Coding

Coded - Design and coding required

Font styles to use
Sans Serif
Other font styles liked:
• We like the combination of OSWALD REGULAR for headlines and MONTSERRAT EXTRA LIGHT or LIGHT for plain text. Deviations which will support a better design are very much welcome.

Colors
0094D4
00A9DD
6FCCEA
C7EBF8
E9F6FB
EB3D1F
EC4F4E
F09395
F8D3D4
FCEDEE

Requirements
Must have
• The design must be adaptable to an event booking function. This can be either achieved by a WordPress plugin such an Event calendar or an Event Wordpress theme (Vorelt is preferred). The design shall but mobile first.
Nice to have
• Create an emotional, welcoming atmosphere. More human than streamlining.
Should not have
• We don't like a cold, too straight or too structured design.

```html
<!DOCTYPE html>
<html lang="de">
<head>
<meta charset="utf-8">
<title>Zusammen für Brockelsdorf e.V.</title>
<link href="https://fonts.googleapis.com/css2?family=Oswald:wght@400;500&family=Montserrat:wght@300;400;500&display=swap" rel="stylesheet">
<style>
:root{
  --blue:#2b4fa3;
  --blue-dark:#213f88;
  --red:#e3283a;
  --text:#222;
  --muted:#555;
  --light:#f4f4f6;
  --white:#fff;
  --teal:#1bb0c9;
}
*{box-sizing:border-box;margin:0;padding:0}
html,body{width:1200px;height:4484px;overflow:hidden}
body{font-family:'Montserrat',sans-serif;color:var(--text);background:var(--white);position:relative}
.abs{position:absolute}
h1,h2,h3,h4,.osw{font-family:'Oswald',sans-serif;font-weight:400}
.btn{position:absolute;font-family:'Oswald',sans-serif;font-size:13px;border-radius:20px;display:flex;align-items:center;justify-content:center}
.btn-blue{background:var(--blue);color:#fff;box-shadow:0 4px 10px rgba(43,79,163,.35)}
.btn-outline{border:2px solid var(--blue);color:var(--blue);background:#fff}
.btn-red{background:var(--red);color:#fff}
.btn-ghost{border:1.5px solid #fff;color:#fff}

/* header */
.site-header{position:absolute;top:0;left:0;width:1200px;height:68px;background:#fff;z-index:5}
.brand{position:absolute;left:200px;top:8px;display:flex;align-items:center;gap:6px}
.brand-dot{width:22px;height:22px;border-radius:50%;background:var(--blue)}
.brand-name{font-family:'Oswald',sans-serif;font-size:14px;color:var(--blue)}
.main-nav{position:absolute;left:442px;top:22px;display:flex;gap:28px;font-family:'Oswald',sans-serif;font-size:13px}
.main-nav .active{color:var(--red)}

/* hero */
.hero{position:absolute;top:68px;left:0;width:1200px;height:540px;background:linear-gradient(110deg,#6b5a55 0%,#8a7566 40%,#a08478 70%,#7c4b4f 100%)}
.hero-shade{position:absolute;inset:0;background:linear-gradient(90deg,rgba(0,0,0,.45),rgba(0,0,0,.1))}
.hero h1{position:absolute;left:200px;top:140px;color:#fff;font-size:44px;line-height:56px}
.play{position:absolute;left:932px;top:206px;width:60px;height:60px;border-radius:50%;background:rgba(255,255,255,.85)}

.section-title{position:absolute;width:1200px;text-align:center;font-size:38px;color:#111}

/* events */
.event-photo{position:absolute;width:342px;height:342px;border-radius:50%;overflow:hidden;border:3px solid #fff;box-shadow:0 0 0 2px var(--blue)}
.event-photo div{width:100%;height:100%}
.event-card{position:absolute;top:870px;width:378px;height:257px;background:#f5f5f5;text-align:center}
.tag{position:absolute;top:-22px;left:50%;transform:translateX(-50%);background:var(--teal);color:#fff;font-family:'Oswald',sans-serif;font-size:9px;padding:5px 12px}
.event-date{margin-top:28px;font-size:11px;color:var(--blue);font-family:'Oswald',sans-serif}
.event-card h3{font-size:22px;margin-top:8px}
.event-card p{font-size:11px;line-height:19px;color:#444;margin:16px 42px 0}

/* stats */
.stats{position:absolute;top:1279px;left:0;width:1200px;height:612px;background:linear-gradient(180deg,#2b4fa3 0%,#3a5cb0 50%,#2a4a98 100%)}
.stat{position:absolute;top:155px;width:260px;text-align:center;color:#fff}
.stat-icon{width:66px;height:60px;margin:0 auto 14px;border-radius:10px;background:rgba(255,255,255,.2)}
.stat h4{font-size:22px}
.stat p{font-size:14px;font-weight:300;color:rgba(255,255,255,.75);line-height:22px;margin-top:8px}

/* values */
.value{position:absolute;left:611px;width:390px}
.value h4{font-size:18px;color:var(--blue);display:flex;align-items:center;gap:14px}
.value p{font-size:11px;line-height:19px;margin:14px 0 0 46px}

/* news */
.news{position:absolute;top:2413px;left:0;width:1200px;height:600px;background:linear-gradient(90deg,#e3283a 0%,#c8304a 40%,#4a5a9e 75%,#5a6fa8 100%)}

/* team */
.team{position:absolute;top:2900px;left:0;width:1200px;height:975px;background:var(--light)}
.member{position:absolute;width:181px;background:#fff;text-align:center;box-shadow:0 2px 8px rgba(0,0,0,.06)}
.member .photo{height:206px;background:linear-gradient(180deg,#8a7a6e,#3b4050 60%,#1f2a44)}
.member .name{font-family:'Oswald',sans-serif;font-size:12px;padding:18px 10px 20px;line-height:17px}
.member.active{background:var(--blue);color:#fff}

/* contact */
.contact{position:absolute;top:3871px;left:0;width:1200px;height:284px;background:var(--blue);overflow:hidden}
.field{position:absolute;background:#fff;border-radius:18px;font-size:10px;color:#555;padding:11px 20px}

/* footer */
.site-footer{position:absolute;top:4155px;left:0;width:1200px;height:329px;background:#f2f2f4}
.foot-col h5{font-family:'Oswald',sans-serif;font-weight:400;font-size:14px;margin-bottom:18px}
.foot-col li{list-style:none;font-size:10px;line-height:18px}
.social{width:24px;height:24px;border-radius:50%;background:var(--blue);display:inline-block;margin-right:6px}
</style>
</head>
<body>

<header class="site-header">
  <div class="brand"><span class="brand-dot"></span><span class="brand-name">Zusammen für Brockelsdorf e.V.</span></div>
  <nav class="main-nav">
    <span class="active">-- Home --</span><span>About Us</span><span>Upcoming Events</span><span>Team</span><span>News</span><span>Shop</span>
  </nav>
  <div class="btn btn-outline" style="left:887px;top:12px;width:113px;height:38px">Contact Us</div>
</header>

<section class="hero">
  <div class="hero-shade" role="img" aria-label="Foto: Vereinsmitglieder bei einem gemeinsamen Frühstück am langen Tisch"></div>
  <h1>Nachbarschaft spüren.<br>In Brockelsdorf daheim!</h1>
  <div class="btn btn-blue" style="left:200px;top:282px;width:110px;height:36px">Contact Us</div>
  <div class="play"><svg width="60" height="60"><circle cx="30" cy="30" r="22" fill="#e3283a"/><path d="M26 21 L38 30 L26 39Z" fill="#fff"/></svg></div>
</section>
<svg class="abs" style="left:0;top:470px" width="1200" height="140">
  <path d="M0 140 Q600 -40 1200 140 Z" fill="#fff"/>
  <path d="M0 132 Q600 -48 1200 132" fill="none" stroke="#2b4fa3" stroke-width="5"/>
</svg>

<h2 class="section-title" style="top:560px">Kommende Veranstaltungen</h2>

<div class="event-photo" style="left:222px;top:653px"><div role="img" aria-label="Foto: Konzertabend mit Lichterdekoration" style="background:linear-gradient(160deg,#2c4a7a,#8a4a3a 60%,#c06040)"></div></div>
<div class="event-photo" style="left:635px;top:653px"><div role="img" aria-label="Foto: Festsaal mit Gästen beim Themenabend" style="background:linear-gradient(160deg,#6a5a4a,#9a7a5a 50%,#4a5a8a)"></div></div>
<div class="abs" style="left:0;top:870px;width:1200px;height:200px;background:#fff"></div>

<article class="event-card" style="left:205px">
  <span class="tag">CULTURAL EVENTS</span>
  <div class="event-date">&#9635; 10.11.2023</div>
  <h3>Mara Quell</h3>
  <p>Mara kehrt zurück! Am 10.11.2023 erneut in der Holunderscheune. Lassen Sie sich von ihrem Mix aus Schlagern und Evergreens mitreißen.</p>
  <div class="btn" style="left:85px;top:194px;width:100px;height:32px;background:#1e88d6;color:#fff">More Info</div>
  <div class="btn btn-red" style="left:192px;top:194px;width:100px;height:32px">Book Events</div>
</article>
<article class="event-card" style="left:618px">
  <span class="tag">CONCERTS</span>
  <div class="event-date">&#9635; 21.11.2023</div>
  <h3>Spanischer Abend</h3>
  <p>La Dolce Vita in Brockelsdorf. Am 21.11.2023 genießen wir in der Holunderscheune authentische italienische Spezialitäten in einer warmen Atmosphäre.</p>
  <div class="btn" style="left:85px;top:194px;width:100px;height:32px;background:#1e88d6;color:#fff">More Info</div>
  <div class="btn btn-red" style="left:192px;top:194px;width:100px;height:32px">Book Events</div>
</article>
<div class="btn btn-outline" style="left:537px;top:1166px;width:126px;height:38px">View All Events</div>

<section class="stats" role="img" aria-label="Hintergrundfoto: Felder in der Abenddämmerung, blau getönt">
  <h2 class="section-title" style="top:65px;color:#fff;font-size:36px">Zusammen für Brockelsdorf e.V.</h2>
  <div class="stat" style="left:194px"><div class="stat-icon"></div><h4>Mitglieder</h4><p>XXX stolze Mitglieder.</p></div>
  <div class="stat" style="left:470px"><div class="stat-icon"></div><h4>Events in 2023</h4><p>XXX Events bisher in diesem Jahr.</p></div>
  <div class="stat" style="left:745px"><div class="stat-icon"></div><h4>Besucher</h4><p>XXX glückliche Besucher bei unseren Veranstaltungen.</p></div>
  <div class="btn btn-ghost" style="left:544px;top:371px;width:112px;height:38px">Contact Us</div>
</section>
<svg class="abs" style="left:0;top:1760px" width="1200" height="135">
  <path d="M0 135 Q600 -60 1200 135 Z" fill="#fff"/>
  <path d="M0 128 Q600 -67 1200 128" fill="none" stroke="#2b4fa3" stroke-width="5"/>
</svg>

<svg class="abs" style="left:198px;top:1898px" width="366" height="440">
  <path d="M258 2 H362 V80" fill="none" stroke="#1e88d6" stroke-width="2"/>
  <path d="M2 350 V438 H90" fill="none" stroke="#e3283a" stroke-width="2"/>
</svg>
<div class="abs" role="img" aria-label="Foto: Menschenmenge bei einem Dorffest unter blauem Himmel" style="left:212px;top:1912px;width:338px;height:413px;border-radius:30px 0 30px 0;background:linear-gradient(180deg,#3f7fd8 0%,#8fb6e6 35%,#7a6a50 65%,#3a3a48 100%)"></div>

<h2 class="abs" style="left:611px;top:1890px;font-size:36px">Werte und Mission</h2>
<div class="value" style="top:1958px"><h4><svg width="20" height="12"><path d="M1 6 L6 11 L13 2 M8 6 L12 11 L19 2" fill="none" stroke="#e3283a" stroke-width="1.6"/></svg>Miteinander in Brockelsdorf stärken</h4><p>Unsere Gemeinschaft ist unser Herzstück. Wir setzen uns dafür ein, dass jeder Einwohner in Brockelsdorf sich zugehörig und geschätzt fühlt.</p></div>
<div class="value" style="top:2065px"><h4><svg width="20" height="12"><path d="M1 6 L6 11 L13 2 M8 6 L12 11 L19 2" fill="none" stroke="#e3283a" stroke-width="1.6"/></svg>Kulturelles Angebot schaffen</h4><p>Kultur belebt! Durch Veranstaltungen, Konzerte und Feste bereichern wir das kulturelle Leben in Brockelsdorf.</p></div>
<div class="value" style="top:2172px"><h4><svg width="20" height="12"><path d="M1 6 L6 11 L13 2 M8 6 L12 11 L19 2" fill="none" stroke="#e3283a" stroke-width="1.6"/></svg>Füreinander da sein</h4><p>In guten wie in schlechten Zeiten – wir stehen zusammen. Egal ob jung oder alt, jeder wird in unserer Gemeinschaft unterstützt.</p></div>
<div class="btn btn-blue" style="left:612px;top:2300px;width:114px;height:38px">Contact Us</div>

<section class="news" role="img" aria-label="Foto: Sommerfest mit Zelten und vielen Besuchern, rot-blau getönt">
  <h2 class="abs osw" style="left:200px;top:68px;font-size:36px;color:#fff">Aktuelle Nachrichten-Highlights</h2>
  <div class="abs osw" style="left:200px;top:146px;font-size:11px;color:#fff">&#9635; 21.06.2023</div>
  <h3 class="abs" style="left:200px;top:168px;font-size:22px;color:#fff">Sommerfest in Brockelsdorf</h3>
  <p class="abs" style="left:200px;top:208px;width:450px;font-size:14px;line-height:22px;color:#fff;font-weight:300">Ein voller Erfolg! Mit über 400 Besuchern feierten wir am 21.06.2023 unser traditionelles Sommerfest inklusive Vogelschießen.</p>
  <div class="abs osw" style="left:200px;top:290px;font-size:12px;color:#fff">Read More &#8594;</div>
  <div class="btn btn-blue" style="left:200px;top:346px;width:112px;height:38px">View All News</div>
  <svg class="abs" style="left:985px;top:212px" width="16" height="78">
    <circle cx="8" cy="8" r="5" fill="none" stroke="#fff" stroke-width="1.5"/>
    <circle cx="8" cy="27" r="5" fill="none" stroke="#fff" stroke-width="1.5"/><circle cx="8" cy="27" r="2.5" fill="#fff"/>
    <circle cx="8" cy="46" r="5" fill="none" stroke="#fff" stroke-width="1.5"/>
    <circle cx="8" cy="65" r="5" fill="none" stroke="#fff" stroke-width="1.5"/>
  </svg>
</section>

<section class="team">
  <svg class="abs" style="left:0;top:-40px" width="1200" height="140">
    <path d="M0 100 Q600 -80 1200 30 V140 H0Z" fill="#f4f4f6"/>
    <path d="M0 100 Q600 -80 1200 30" fill="none" stroke="#2b4fa3" stroke-width="5"/>
  </svg>
  <h2 class="section-title" style="top:45px;font-size:36px">Unser engagiertes Team</h2>
  <p class="abs" style="left:0;top:105px;width:1200px;text-align:center;font-size:14px;color:#444">Lernen Sie die Köpfe hinter 'Zusammen für Brockelsdorf e.V.' kennen.</p>
  <div class="member" style="left:200px;top:164px"><div class="photo" role="img" aria-label="Porträtfoto Vorstandsmitglied"></div><div class="name">JANA WEHRMANN</div></div>
  <div class="member active" style="left:406px;top:164px"><div class="photo" role="img" aria-label="Porträtfoto Vorstandsmitglied"></div><div class="name">HEIKE LINDQVIST</div></div>
  <div class="member" style="left:613px;top:164px"><div class="photo" role="img" aria-label="Porträtfoto Vorstandsmitglied"></div><div class="name">BERND<br>OHLSEN-WEHRMANN</div></div>
  <div class="member" style="left:819px;top:164px"><div class="photo" role="img" aria-label="Porträtfoto Vorstandsmitglied"></div><div class="name">JÖRG TAMSEN</div></div>
  <div class="member" style="left:303px;top:495px"><div class="photo" role="img" aria-label="Porträtfoto Vorstandsmitglied"></div><div class="name">UWE<br>HARMSEN</div></div>
  <div class="member" style="left:509px;top:495px"><div class="photo" role="img" aria-label="Porträtfoto Vorstandsmitglied"></div><div class="name" style="padding-top:24px">SILKE<br>BRANDHORST</div></div>
  <div class="member" style="left:716px;top:495px"><div class="photo" role="img" aria-label="Porträtfoto Vorstandsmitglied"></div><div class="name">MARC BRANDHORST</div></div>
  <div class="btn btn-outline" style="left:544px;top:835px;width:112px;height:38px">Contact Us</div>
</section>

<section class="contact">
  <h2 class="abs" style="left:200px;top:72px;font-size:36px;color:#fff">Wir sind für Sie da!</h2>
  <p class="abs" style="left:200px;top:148px;width:400px;font-size:14px;line-height:22px;color:#fff;font-weight:300">Haben Sie Fragen, Anregungen oder möchten Sie uns unterstützen? Kontaktieren Sie uns – wir freuen uns auf Ihre Nachricht."</p>
</section>
<svg class="abs" style="left:628px;top:3843px" width="450" height="312">
  <circle cx="225" cy="227" r="223" fill="#2b4fa3" stroke="#fff" stroke-width="4"/>
</svg>
<div class="field" style="left:694px;top:3934px;width:150px;height:32px">Your Name</div>
<div class="field" style="left:857px;top:3934px;width:150px;height:32px">Phone</div>
<div class="field" style="left:694px;top:3978px;width:313px;height:32px">Email</div>
<div class="field" style="left:694px;top:4022px;width:313px;height:78px">Type your Message ..</div>
<div class="btn btn-red" style="left:612px;top:4128px;width:481px;height:37px">Submit</div>

<footer class="site-footer">
  <div class="abs" style="left:204px;top:90px;display:flex;align-items:center;gap:6px"><span class="brand-dot"></span><span class="brand-name">Zusammen für Brockelsdorf e.V.</span></div>
  <div class="abs foot-col" style="left:469px;top:75px">
    <h5>Kontaktiere uns</h5>
    <ul>
      <li style="font-size:13px;margin-bottom:8px"><span style="color:var(--red)">&#9990;</span>&nbsp; 040-555-0172</li>
      <li style="margin-bottom:8px"><span style="color:var(--red)">&#9993;</span>&nbsp; vorstand@zfbev-beispiel.de</li>
      <li style="line-height:13px"><span style="color:var(--red)">&#9679;</span>&nbsp; Zusammen für Brockelsdorf eV<br>&nbsp;&nbsp;&nbsp;&nbsp;Am Dorfteich 4 21999<br>&nbsp;&nbsp;&nbsp;&nbsp;Brockelsdorf</li>
    </ul>
  </div>
  <div class="abs foot-col" style="left:719px;top:75px">
    <h5>Quicklinks</h5>
    <ul><li>Home</li><li>About Us</li><li>Upcoming Events</li><li>Team</li><li>News</li><li>Contact Us</li></ul>
  </div>
  <div class="abs foot-col" style="left:882px;top:75px">
    <h5>Follow Us</h5>
    <span class="social"></span><span class="social" style="background:var(--red)"></span><span class="social"></span><span class="social"></span>
  </div>
  <p class="abs" style="left:0;top:300px;width:1200px;text-align:center;font-size:9px;color:#444">© 2023 <span style="color:var(--red);font-weight:500">ZUSAMMEN FÜR BROCKELSDORF E.V.</span> All Rights Reserved</p>
</footer>

</body>
</html>
```